Design Executive Business Acquisitons Brokerage Website

Modern but Professional with the colours black, purple and white. Must convey authenticity, and progressive out-of-square thinking. We are a boutique Business Broking firm located in Brisbane QLD Australia. We market and sell businesses with sales revenue/turnover from Au $1M to $15 M + or have a minimum staff of 15 to 50 staff. Our buyers are generally acquisitions corporate buyers. We need a modern approach but conservative tones. We are serious and experienced. We say it as it is and we get the job done! We sell in the following industries but not limited to, engineering, manufacturing, agriculture, recruitment, transportation, warehousing, services, IT,eCommerce, civil construction,mining, wholesaling, dealerships, MEdical (all), service stations, Management rights, high-end retail, building construction,importing,exporting to name a few.

Target Market(s)

SME Corporate Public & Private exsisting large businesses that are looking to buy through acquisitions

Industry/Entity Type

Coommercial executive Business Sale

Number of Pages Required

5+ page

Font styles to use
Sans Serif

Requirements
Must have
• Serious tones, searchar, NDA form, serious corporate executive feel. Include all corporaate colors,black less whit purples.Corporate Logo
Nice to have
• carosel moving right to left of industry pictures as per above and attached industries
Should not have
• No hand shaking, business people.

```html
<!DOCTYPE html>
<html lang="en">
<head>
<meta charset="utf-8">
<title>Meridian Acquisitions Group</title>
<link href="https://fonts.googleapis.com/css2?family=Roboto:wght@400;500;700;900&display=swap" rel="stylesheet">
<style>
:root{
  --purple:#4f3a7e;
  --purple-dark:#3f2d69;
  --ink:#333236;
  --charcoal:#414044;
  --grey-text:#8a8a8e;
  --page:#f1f1f3;
  --white:#ffffff;
}
*{box-sizing:border-box;margin:0;padding:0}
html,body{width:1200px;height:3715px;overflow:hidden}
body{font-family:'Roboto',sans-serif;background:var(--page);color:var(--ink)}
.canvas{position:relative;width:1200px;height:3715px;overflow:hidden;background:linear-gradient(180deg,#f6f6f8,#ececef)}
.abs{position:absolute}
svg.abs{display:block}

/* header */
.brand{position:absolute;left:145px;top:34px;display:flex;align-items:center;gap:12px}
.brand-dot{width:44px;height:44px;border-radius:50%;background:var(--purple);flex:none}
.brand-name{font-weight:700;font-size:21px;line-height:1;color:var(--purple);white-space:nowrap}
.nav{position:absolute;top:51px;left:552px;font-size:14px;font-weight:500;color:#2b2a30}
.nav a{position:absolute;white-space:nowrap;text-decoration:none;color:inherit}
.btn{display:flex;align-items:center;justify-content:center;border-radius:30px;font-weight:500;text-decoration:none;white-space:nowrap}
.btn-login{position:absolute;left:959px;top:39px;width:97px;height:42px;background:var(--purple);color:#fff;font-size:14px}

/* hero */
.hero-photo{position:absolute;left:0;top:0;width:1200px;height:760px;background:linear-gradient(180deg,#c9d2e2 0%,#8f9fbc 12%,#5c6d94 30%,#3a3f6a 48%,#6a5a6c 60%,#a27a5c 72%,#4b4a5e 86%,#2c2f45 100%)}
.hero-ring{position:absolute;left:413px;top:199px;width:374px;height:374px;border-radius:50%;background:rgba(255,255,255,.22)}
.hero-disc{position:absolute;left:441px;top:227px;width:318px;height:318px;border-radius:50%;background:rgba(58,56,60,.93)}
.hero-title{position:absolute;left:400px;top:292px;width:400px;text-align:center;color:#fff;font-weight:900;font-size:48px;line-height:52px}
.btn-start{position:absolute;left:533px;top:471px;width:134px;height:40px;background:var(--purple);border:2px solid #fff;color:#fff;font-size:14px}
.dots{position:absolute;left:573px;top:634px;display:flex;gap:12px}
.dots span{width:9px;height:9px;border-radius:50%;background:#fff}
.dots span.off{background:transparent;border:2px solid #fff}

/* section titles */
.section-title{position:absolute;left:0;width:1200px;text-align:center;font-weight:900;font-size:41px;color:var(--ink)}
.bar{position:absolute;height:5px;width:43px;background:var(--purple)}

/* services */
.svc-ring{position:absolute;border-radius:50%;background:#fff}
.svc-ring.purple{border:16px solid var(--purple)}
.svc-ring.dark{border:16px solid var(--charcoal)}
.svc-text{position:absolute;width:195px}
.svc-text h3{font-size:15px;font-weight:500;line-height:21px;color:#2b2a30;margin-bottom:16px}
.svc-text p{font-size:13px;line-height:19px;color:var(--grey-text);text-align:justify}

/* about */
.about-title{position:absolute;left:147px;top:1645px;font-size:42px;font-weight:900;color:#fff}
.about-copy{position:absolute;left:147px;top:1749px;width:433px;font-size:14px;line-height:26.6px;color:#fff}
.btn-ghost{position:absolute;left:147px;top:2007px;width:134px;height:41px;border:2px solid #fff;color:#fff;font-size:14px}
.feature{position:absolute;display:flex;align-items:center;gap:18px;color:#fff;font-weight:700;font-size:18px}

/* blog */
.card{position:absolute;background:#fff;border-radius:22px;overflow:hidden;box-shadow:0 3px 12px rgba(0,0,0,.08)}
.card-img{position:absolute}
.card-body{position:absolute}
.date{font-size:13px;color:#333}
.card-body h3{font-size:20px;font-weight:700;line-height:25px;color:#222;margin-top:14px}
.card-body p{font-size:13px;line-height:25.5px;color:var(--grey-text);margin-top:14px}
.more{display:block;font-size:15px;font-weight:700;color:var(--purple);margin-top:14px}
.btn-blogs{position:absolute;left:509px;top:3033px;width:182px;height:39px;background:var(--purple);color:#fff;font-size:14px}

/* newsletter & footer */
.footer-bg{position:absolute;left:0;top:3170px;width:1200px;height:545px}
.newsletter{position:absolute;left:147px;top:3156px;width:906px;height:141px;background:var(--purple)}
.newsletter h2{position:absolute;left:36px;top:36px;font-size:42px;font-weight:900;color:#fff;white-space:nowrap}
.newsletter .bar{left:36px;top:104px;background:#fff}
.email{position:absolute;left:519px;top:43px;width:351px;height:42px;background:#fff;border-radius:22px}
.email span{position:absolute;left:16px;top:13px;font-size:13px;color:#999}
.email b{position:absolute;right:4px;top:4px;width:92px;height:34px;border-radius:18px;background:var(--charcoal);color:#fff;font-size:14px;font-weight:500;display:flex;align-items:center;justify-content:center}
.foot-col{position:absolute;color:#fff}
.foot-col h4{font-size:20px;font-weight:500;margin-bottom:16px}
.foot-col a{display:block;font-size:16px;line-height:32px;color:#fff;text-decoration:none}
.divider{position:absolute;width:1px;background:rgba(255,255,255,.35)}
.foot-brand{position:absolute;left:0;width:1200px;top:3395px;display:flex;align-items:center;justify-content:center;gap:14px}
.foot-brand .brand-dot{width:48px;height:48px;background:#fff}
.foot-brand .brand-name{color:#fff;font-size:24px}
.social{position:absolute;width:50px;height:50px;border-radius:50%;border:2px solid #fff}
.copyright{position:absolute;left:0;top:3650px;width:1200px;text-align:center;font-size:15px;color:#fff}
</style>
</head>
<body>
<div class="canvas">

  <!-- hero -->
  <div class="hero-photo" role="img" aria-label="Dusk city skyline with a lit steel bridge over a river"></div>
  <svg class="abs" style="left:0;top:660px" width="1200" height="140" viewBox="0 0 1200 140">
    <path d="M0 50 C120 110 250 100 380 60 C500 20 560 15 650 40 C760 70 820 105 960 95 C1060 88 1130 60 1200 30 L1200 140 L0 140 Z" fill="#f5f5f7"/>
  </svg>

  <header>
    <div class="brand"><span class="brand-dot"></span><span class="brand-name">Meridian Acquisitions Group</span></div>
    <nav class="nav">
      <a style="left:0">HOME</a>
      <a style="left:70px">ABOUT</a>
      <a style="left:145px">SERVICES</a>
      <a style="left:240px">NEWS</a>
      <a style="left:309px">CONTACT</a>
    </nav>
    <a class="btn btn-login">LOGIN</a>
  </header>

  <div class="hero-ring"></div>
  <div class="hero-disc"></div>
  <h1 class="hero-title">MERIDIAN<br>ACQUISITIONS<br>GROUP</h1>
  <a class="btn btn-start">GET STARTED</a>
  <div class="dots"><span></span><span class="off"></span><span></span></div>

  <!-- services -->
  <h2 class="section-title" style="top:790px">OUR SERVICES</h2>
  <div class="bar" style="left:579px;top:853px"></div>

  <svg class="abs" style="left:0;top:1050px" width="1200" height="150" viewBox="0 1050 1200 150">
    <path d="M147 1100 C230 1150 380 1148 479 1144 C560 1140 620 1128 692 1129 C820 1130 860 1185 960 1168 C1010 1158 1040 1130 1053 1113" fill="none" stroke="#a9a7b3" stroke-width="3" stroke-dasharray="2 6" stroke-linecap="round"/>
    <circle cx="147" cy="1100" r="8" fill="#3d3c40"/>
    <circle cx="479" cy="1144" r="8" fill="#4f3a7e"/>
    <circle cx="692" cy="1129" r="8" fill="#4f3a7e"/>
    <circle cx="1053" cy="1113" r="8" fill="#3d3c40"/>
  </svg>

  <div class="svc-ring purple" style="left:177px;top:940px;width:168px;height:168px"></div>
  <svg class="abs" style="left:221px;top:984px" width="80" height="80" viewBox="0 0 80 80" fill="none" stroke="#333" stroke-width="3">
    <circle cx="40" cy="40" r="34"/><circle cx="40" cy="40" r="24"/>
    <text x="40" y="51" text-anchor="middle" font-family="Roboto,sans-serif" font-size="30" fill="#333" stroke="none" font-weight="700">$</text>
  </svg>
  <div class="svc-text" style="left:412px;top:941px"><h3>NEMO ENIM IPSAM VOLUPTATEM</h3><p>Sed ut perspiciatis unde omnis iste natus error sit voluptatem accusantiumm, totam rem premque laudantium, totam rem periam, eaque ipsa quae ab</p></div>

  <div class="svc-ring dark" style="left:649px;top:940px;width:168px;height:168px"></div>
  <svg class="abs" style="left:693px;top:984px" width="80" height="80" viewBox="0 0 80 80" fill="none" stroke="#4f3a7e" stroke-width="3" stroke-linejoin="round">
    <rect x="36" y="6" width="36" height="26" rx="3"/>
    <text x="54" y="27" text-anchor="middle" font-family="Roboto,sans-serif" font-size="20" fill="#4f3a7e" stroke="none" font-weight="700">$</text>
    <path d="M8 56 L24 48 L46 50 L60 44 L68 50 L48 66 L8 70 Z"/>
  </svg>
  <div class="svc-text" style="left:854px;top:949px"><h3>EXCEPTEUR SINT OCC AECAT CUPIDATAT</h3><p>Sed ut perspiciatis unde omnis iste natus error sit voluptatem accusantiumm, totam rem premque laudantium, totam rem periam, eaque ipsa quae ab</p></div>

  <div class="svc-text" style="left:177px;top:1176px"><h3>ACCUSANTIUM DOL OREMQUE</h3><p>Sed ut perspiciatis unde omnis iste natus error sit voluptatem accusantiumm, totam rem premque laudantium, totam rem periam, eaque ipsa quae ab</p></div>
  <div class="svc-ring dark" style="left:409px;top:1165px;width:168px;height:168px"></div>
  <svg class="abs" style="left:453px;top:1209px" width="80" height="80" viewBox="0 0 80 80" fill="none" stroke="#4f3a7e" stroke-width="3" stroke-linejoin="round">
    <path d="M6 38 L40 12 L74 38"/><rect x="14" y="36" width="52" height="36"/>
    <rect x="20" y="46" width="12" height="12"/><rect x="48" y="46" width="12" height="12"/><rect x="35" y="52" width="10" height="20"/>
    <circle cx="40" cy="12" r="9" fill="#fff"/>
  </svg>
  <div class="svc-text" style="left:642px;top:1176px"><h3>NEMO ENIM IPSAM VOL UPTATEM QUIA</h3><p>Sed ut perspiciatis unde omnis iste natus error sit voluptatem accusantiumm, totam rem premque laudantium, totam rem periam, eaque ipsa quae ab</p></div>
  <div class="svc-ring purple" style="left:856px;top:1171px;width:168px;height:168px"></div>
  <svg class="abs" style="left:900px;top:1215px" width="80" height="80" viewBox="0 0 80 80" fill="none" stroke="#333" stroke-width="3" stroke-linejoin="round">
    <rect x="8" y="34" width="64" height="34" rx="3"/><path d="M8 44 H72"/>
    <circle cx="40" cy="18" r="10"/>
    <path d="M40 34 V28"/>
  </svg>

  <!-- about -->
  <svg class="abs" style="left:0;top:1440px" width="1200" height="820" viewBox="0 0 1200 820" role="presentation">
    <defs><linearGradient id="aboutFill" x1="0" y1="0" x2="0" y2="1"><stop offset="0" stop-color="#573f8a"/><stop offset="1" stop-color="#4b3b6b"/></linearGradient></defs>
    <path d="M0 100 C40 112 80 120 138 126 C260 70 420 10 600 6 C800 2 980 50 1115 118 C1150 108 1180 96 1200 90 L1200 720 C1100 740 950 760 760 730 C560 700 360 690 160 775 C100 800 40 810 0 812 Z" fill="url(#aboutFill)"/>
  </svg>
  <h2 class="about-title">ABOUT US</h2>
  <div class="bar" style="left:147px;top:1706px;background:#fff"></div>
  <p class="about-copy">Lorem ipsum dolor sit amet, consectetur adipiscing elit, sed do eius-mod tempor incididunt ut labore et dolore magna aliqua. Quis ipsum suspendisse ultrices gravida. Risus commodo viverra maecenas accumsan lacus vel facilisisLorem ipsum dolor sit ameonsectetur adipiscing elit, sed do eiusmod tempor incididunt ut labore et dolore magna aliq ipsum suspendisse ultricesgravidaisusommodo viverra mausmod tempor incididunt ut labore et dolore magna aliq ipsum suspendisse ultricesge</p>
  <a class="btn btn-ghost">READ MORE</a>

  <svg class="abs" style="left:600px;top:1620px" width="470" height="470" viewBox="600 1620 470 470">
    <defs><linearGradient id="band" x1="0" y1="0" x2="1" y2="0"><stop offset="0" stop-color="#161518"/><stop offset=".6" stop-color="#3a393d"/><stop offset="1" stop-color="#77767a"/></linearGradient></defs>
    <path d="M1030 1693 L1012 1734 L760 1734 Z" fill="#1c1b1e"/>
    <path d="M990 1800 L978 1843 L730 1843 Z" fill="#1c1b1e"/>
    <path d="M960 1907 L943 1950 L760 1950 Z" fill="#1c1b1e"/>
    <path d="M920 2013 L834 2080 L834 2013 Z" fill="#1c1b1e"/>
    <path d="M617 1627 L1050 1627 L1030 1693 L635 1693 Z" fill="url(#band)"/>
    <path d="M656 1734 L1012 1734 L990 1800 L672 1800 Z" fill="url(#band)"/>
    <path d="M688 1843 L978 1843 L960 1907 L704 1907 Z" fill="url(#band)"/>
    <path d="M724 1950 L943 1950 L920 2013 L738 2013 Z" fill="url(#band)"/>
    <g fill="none" stroke="#fff" stroke-width="2">
      <rect x="670" y="1648" width="24" height="24" rx="3"/><path d="M674 1666 L682 1658 L690 1662"/>
      <circle cx="708" cy="1767" r="16"/><path d="M700 1775 L716 1759"/><circle cx="702" cy="1761" r="2.5"/><circle cx="714" cy="1773" r="2.5"/>
      <circle cx="744" cy="1881" r="12"/><path d="M726 1862 L762 1862"/>
      <rect x="750" y="1966" width="26" height="22"/><circle cx="780" cy="1990" r="9"/>
    </g>
  </svg>
  <div class="feature" style="left:744px;top:1650px">NEMO ENIM IPSIM IPSAMAM</div>
  <div class="feature" style="left:748px;top:1757px">ACCUSANTIUM DOLOMQUE</div>
  <div class="feature" style="left:783px;top:1861px">COMMOONSEQUAT</div>
  <div class="feature" style="left:805px;top:1968px">LIQUIPXEAC</div>

  <!-- blog -->
  <h2 class="section-title" style="top:2327px">FROM THE BLOG</h2>
  <div class="bar" style="left:579px;top:2391px"></div>

  <article class="card" style="left:141px;top:2449px;width:296px;height:508px">
    <div class="card-img" style="left:3px;top:3px;width:290px;height:221px;border-radius:20px;background:linear-gradient(135deg,#e7e4df,#9aa3ad 55%,#3a4150)" role="img" aria-label="Colleagues reviewing documents at a laptop"></div>
    <div class="card-body" style="left:22px;top:255px;width:256px">
      <div class="date">June 22,2022</div>
      <h3>Sed ut perspiciatis unde omnis iste natus</h3>
      <p>Ut enim ad minima venuis nostreierci tationem ullam corporis slaboriosan isi ut aliquid ex ea commodi eprehenderitq ui in ea voluptate velit .</p>
      <span class="more">READ MORE</span>
    </div>
  </article>

  <article class="card" style="left:456px;top:2449px;width:603px;height:245px">
    <div class="card-img" style="left:0;top:0;width:237px;height:245px;border-radius:20px;background:linear-gradient(135deg,#e9e6e0,#b9b3a8 50%,#2d2f38)" role="img" aria-label="Laptop showing a market chart on a desk"></div>
    <div class="card-body" style="left:268px;top:28px;width:310px">
      <div class="date">June 22,2022</div>
      <h3>Sed ut perspiciatis unde omnis iste natus error</h3>
      <p style="margin-top:10px">Ut enim ad minima veniam, quis nostreierci tationem ullam corporis suscipit laboriosan isi ut aliquid ex ea eprehenderitq utate velit .</p>
      <span class="more" style="margin-top:8px">READ MORE</span>
    </div>
  </article>

  <article class="card" style="left:456px;top:2712px;width:603px;height:245px">
    <div class="card-img" style="left:0;top:0;width:237px;height:245px;border-radius:20px;background:linear-gradient(135deg,#d9dbe0,#f3f2ef 50%,#8e8f92)" role="img" aria-label="Small model house beside a signed contract and keys"></div>
    <div class="card-body" style="left:268px;top:28px;width:310px">
      <div class="date">June 22,2022</div>
      <h3>Sed ut perspiciatis unde omnis iste natus error</h3>
      <p style="margin-top:10px">Ut enim ad minima veniam, quis nostreierci tationem ullam corporis suscipit laboriosan isi ut aliquid ex ea eprehenderitq utate velit .</p>
      <span class="more" style="margin-top:8px">READ MORE</span>
    </div>
  </article>

  <svg class="abs" style="left:140px;top:3020px" width="920" height="80" viewBox="140 3020 920 80">
    <path d="M148 3030 C180 3060 300 3075 509 3062" fill="none" stroke="#a9a7b3" stroke-width="3" stroke-dasharray="2 6" stroke-linecap="round"/>
    <path d="M691 3047 C800 3055 900 3110 1052 3036" fill="none" stroke="#a9a7b3" stroke-width="3" stroke-dasharray="2 6" stroke-linecap="round"/>
  </svg>
  <a class="btn btn-blogs">VIEW MORE BLOGS</a>

  <!-- footer -->
  <svg class="footer-bg" viewBox="0 0 1200 545" preserveAspectRatio="none">
    <path d="M0 90 C300 30 500 10 700 20 C900 30 1080 50 1200 30 L1200 545 L0 545 Z" fill="#413f45"/>
  </svg>

  <section class="newsletter">
    <h2>SIGN UP NEWSLETTER</h2>
    <div class="bar"></div>
    <div class="email"><span>Enter Email</span><b>SIGN UP</b></div>
  </section>

  <div class="foot-col" style="left:182px;top:3367px"><h4>QUICK LINKS</h4><a>Home</a><a>About</a><a>Services</a><a>News</a><a>Contact</a></div>
  <div class="divider" style="left:376px;top:3361px;height:216px"></div>
  <div class="foot-brand"><span class="brand-dot"></span><span class="brand-name">Meridian Acquisitions Group</span></div>
  <div class="social" style="left:471px;top:3487px" role="img" aria-label="Social profile link"></div>
  <div class="social" style="left:539px;top:3487px" role="img" aria-label="Social profile link"></div>
  <div class="social" style="left:607px;top:3487px" role="img" aria-label="Video channel link"></div>
  <div class="social" style="left:673px;top:3487px" role="img" aria-label="Photo profile link"></div>
  <div class="divider" style="left:832px;top:3361px;height:216px"></div>
  <div class="foot-col" style="left:887px;top:3367px"><h4>OTHER LINKS</h4><a>Terms and Use</a><a>Privacy Policy</a><a>Information</a><a>Sitemap</a></div>

  <p class="copyright">Meridian Acquisitions Group. All rights reserved.Privacy Terms of Use&nbsp; 2022 ©</p>
</div>
</body>
</html>
```